Tobin's Butter dairy product for export market

We are starting a new brand for our butter range. We are looking for a premimum branding with family values. The product should be elligent and simle and easy for consumers to choose and easy for chefs,

A samples of our current brand and packing details in on the pack
target markets , China, Hong Kong, Asia, middle east
products will be sold in different size starting from small portion eg 7g to 1kg food service pack
product will be sold in 2 varients salted and unsalted

Target Market(s)

Australian Market and export market

Industry/Entity Type

Product

Colors
9bcb3c
fbed22

Requirements
Must have
• Pure butter
• packed in Australia
• nice fresh modern simple design
Nice to have
• Colours gold , green or any other suggestions welcome.
Should not have
• Any third party pictures of butter etc..

```html
<!DOCTYPE html>
<html lang="en">
<head>
<meta charset="utf-8">
<title>Tobin's Butter – Salted Butter 500g pack</title>
<link href="https://fonts.googleapis.com/css2?family=Libre+Baskerville:wght@400;700&family=Share+Tech+Mono&display=swap" rel="stylesheet">
<style>
  :root {
    --backdrop: #ecebee;
    --pack-green: #8cc63f;
    --pack-stripe: #7fb838;
    --ink-green: #1f6b35;
    --burst-yellow: #fbed22;
    --burst-gold: #f0d81c;
    --print-grey: #4d5a3a;
  }
  * { margin: 0; padding: 0; box-sizing: border-box; }
  html, body {
    width: 1200px;
    height: 864px;
    overflow: hidden;
    background: var(--backdrop);
  }
  .canvas {
    position: relative;
    width: 1200px;
    height: 864px;
    display: flex;
    align-items: center;
    justify-content: center;
  }
  .pack-front {
    position: relative;
    width: 780px;
    height: 470px;
    background: var(--pack-green);
    overflow: hidden;
  }
  .pack-stripes {
    position: absolute;
    top: 0;
    left: 360px;
    width: 250px;
    height: 100%;
    background: repeating-linear-gradient(90deg,
      var(--pack-stripe) 0 26px,
      transparent 26px 52px);
  }
  .print-code {
    position: absolute;
    left: 40px;
    top: 60px;
    font-family: "Share Tech Mono", monospace;
    font-size: 15px;
    line-height: 1.35;
    color: var(--print-grey);
    letter-spacing: 0.5px;
  }
  .brand-block {
    position: absolute;
    left: 300px;
    top: 40px;
    width: 380px;
    height: 390px;
  }
  .brand-name {
    position: absolute;
    left: 0;
    top: 20px;
    width: 380px;
    text-align: center;
    font-family: "Libre Baskerville", serif;
    font-weight: 400;
    font-size: 56px;
    line-height: 1;
    color: var(--ink-green);
  }
  .hero-illustration {
    position: absolute;
    left: 50px;
    top: 100px;
    width: 280px;
    height: 200px;
    border-radius: 50%;
    background: radial-gradient(ellipse at 50% 50%,
      var(--burst-yellow) 0%,
      var(--burst-gold) 55%,
      rgba(251, 237, 34, 0) 100%);
  }
  .variant {
    position: absolute;
    left: 0;
    top: 318px;
    width: 380px;
    text-align: center;
    font-family: "Libre Baskerville", serif;
    font-weight: 400;
    font-size: 20px;
    letter-spacing: 6px;
    text-transform: uppercase;
    color: var(--ink-green);
  }
  .net-weight {
    position: absolute;
    left: 40px;
    bottom: 36px;
    font-family: "Libre Baskerville", serif;
    font-weight: 400;
    font-size: 20px;
    color: var(--ink-green);
  }
</style>
</head>
<body>
  <main class="canvas">
    <section class="pack-front">
      <div class="pack-stripes"></div>

      <p class="print-code">2277016 F<br>BEST BEFORE 09/08/2017</p>

      <div class="brand-block">
        <h1 class="brand-name">Tobin's</h1>
        <div class="hero-illustration" role="img" aria-label="Yellow starburst behind a block of butter on a white plate"></div>
        <p class="variant">Salted Butter</p>
      </div>

      <p class="net-weight">500g</p>
    </section>
  </main>
</body>
</html>
```